Higher co-efficient of performance means more heat for your money

I need a bar graph that will have the following heating systems, 80% efficient gas furnace COP of .8, Electric heat COP of 1, and Our best selling heat pump with a cop of 4 at 47F. I will have a constant bar, 100$ worth of gas for furnace, 100$ of electricity for electric heat, and 100$ worth of electricity for our heat pumps. next to them I will have a bar showing how much heat each heating system will provide for $100 of fuel. For gas furnace I need a bar that says $80 worth of heat and the barograph to match it, for electric heat I need the bar to show 100$ worth of heat, for our best selling heat pump I need the bar graph to show and say $400 dollars worth of heat. Please take a look at my website www.summitbreezecomfort.example for brand color and feel

```html
<!DOCTYPE html>
<html lang="en">
<head>
<meta charset="utf-8">
<title>More Heat for Your Money – Summit Breeze Comfort</title>
<link href="https://fonts.googleapis.com/css2?family=Montserrat:ital,wght@0,300;0,400;0,600;0,700;0,800;1,300;1,400;1,700;1,800&display=swap" rel="stylesheet">
<style>
  :root{
    --brand-blue:#0a72ba;
    --axis-blue:#3d8fd0;
    --brand-red:#cc2229;
    --grid-red:#f4d9d9;
    --paper:#ffffff;
    --ink-white:#ffffff;
  }
  *{margin:0;padding:0;box-sizing:border-box}
  html,body{width:1200px;height:1200px;overflow:hidden;background:var(--paper)}
  body{font-family:"Montserrat",sans-serif;position:relative}
  .headline{position:absolute;left:135px;top:68px;font-size:40px;font-weight:700;line-height:48px;color:var(--brand-blue);letter-spacing:-0.2px}
  .headline .accent{color:var(--brand-red)}
  .headline-rule{position:absolute;left:136px;top:216px;width:97px;height:13px;background:var(--brand-red)}
  .brand{position:absolute;left:805px;top:88px;width:210px;display:flex;flex-direction:column;align-items:center;color:var(--brand-red);font-weight:700;text-align:center}
  .brand-dot{width:54px;height:54px;border-radius:50%;background:var(--brand-red);margin-bottom:12px}
  .brand-name{font-size:19px;line-height:22px;letter-spacing:1.5px}
  .chart{position:absolute;left:0;top:0}
  .system-label{position:absolute;top:989px;height:86px;background:var(--brand-blue);border-radius:0 0 22px 22px;color:var(--ink-white);font-weight:700;font-size:26px;line-height:28px;display:flex;align-items:center;justify-content:center;text-align:center}
  .cop-row{position:absolute;top:1088px;height:35px;display:flex;align-items:center;justify-content:center}
  .cop-row::before{content:"";position:absolute;left:0;right:0;top:17px;height:2px;background:var(--brand-blue)}
  .cop-pill{position:relative;background:var(--brand-blue);color:var(--ink-white);font-weight:700;font-size:21px;padding:0 16px;height:35px;line-height:35px;border-radius:9px;width:141px;text-align:center}
  .cop-note{position:absolute;top:1128px;left:0;width:1200px;text-align:center;font-size:31px;font-style:italic;font-weight:300;color:var(--brand-blue)}
  .cop-note b{font-weight:800}
  .disclaimer{position:absolute;top:964px;left:456px;width:285px;text-align:center;font-size:16px;font-style:italic;font-weight:700;color:var(--brand-red)}
</style>
</head>
<body>
  <h1 class="headline">Higher Co-Efficient of<br>Performance means more<br><span class="accent">heat for your money</span></h1>
  <div class="headline-rule"></div>

  <div class="brand">
    <div class="brand-dot"></div>
    <div class="brand-name">SUMMIT BREEZE<br>COMFORT</div>
  </div>

  <svg class="chart" width="1200" height="1200" viewBox="0 0 1200 1200">
    <defs>
      <pattern id="grid" width="28" height="28" patternUnits="userSpaceOnUse" x="0" y="959">
        <path d="M28 0V28M0 28H28" fill="none" stroke="#f4d9d9" stroke-width="1"/>
      </pattern>
      <linearGradient id="fadeUp" x1="0" y1="1" x2="0" y2="0">
        <stop offset="0" stop-color="#fff" stop-opacity="1"/>
        <stop offset="0.6" stop-color="#fff" stop-opacity="0.7"/>
        <stop offset="1" stop-color="#fff" stop-opacity="0"/>
      </linearGradient>
      <mask id="gridMask"><rect x="0" y="291" width="1200" height="668" fill="url(#fadeUp)"/></mask>
      <linearGradient id="railBlue" x1="0" y1="1" x2="0" y2="0">
        <stop offset="0" stop-color="#0a72ba"/>
        <stop offset="1" stop-color="#0a72ba" stop-opacity="0"/>
      </linearGradient>
      <linearGradient id="barRed" x1="0" y1="0" x2="0" y2="1">
        <stop offset="0" stop-color="#cc2229"/>
        <stop offset="1" stop-color="#d4553c"/>
      </linearGradient>
      <pattern id="hatch" width="8" height="8" patternUnits="userSpaceOnUse" patternTransform="rotate(-45)">
        <line x1="0" y1="0" x2="0" y2="8" stroke="#ffffff" stroke-opacity="0.18" stroke-width="1.5"/>
      </pattern>
      <g id="callout-shape">
        <polygon points="8,0 152,0 144,56 0,56" fill="#cc2229"/>
        <polygon points="100,55 126,55 100,78" fill="#cc2229"/>
      </g>
    </defs>

    <!-- grid -->
    <g mask="url(#gridMask)">
      <rect x="139" y="291" width="296" height="668" fill="url(#grid)"/>
      <rect x="456" y="291" width="285" height="668" fill="url(#grid)"/>
      <rect x="763" y="291" width="298" height="668" fill="url(#grid)"/>
    </g>

    <!-- panel rails -->
    <g fill="url(#railBlue)">
      <rect x="137" y="291" width="4" height="670"/><rect x="433" y="291" width="4" height="670"/>
      <rect x="454" y="291" width="4" height="670"/><rect x="739" y="291" width="4" height="670"/>
      <rect x="761" y="291" width="4" height="670"/><rect x="1059" y="291" width="4" height="670"/>
    </g>
    <g fill="#0a72ba">
      <rect x="137" y="957" width="300" height="4"/>
      <rect x="454" y="957" width="289" height="4"/>
      <rect x="761" y="957" width="302" height="4"/>
    </g>

    <!-- y axis -->
    <g font-family="Montserrat, sans-serif" font-weight="700" font-size="24" text-anchor="end">
      <text x="116" y="412" fill="#cfe2f3">$ 400</text>
      <text x="116" y="551" fill="#a9cdea">$ 300</text>
      <text x="116" y="691" fill="#5fa3d8">$ 200</text>
      <text x="116" y="830" fill="#0a72ba">$ 100</text>
      <rect x="126" y="402" width="10" height="3" fill="#cfe2f3"/>
      <rect x="126" y="541" width="10" height="3" fill="#a9cdea"/>
      <rect x="126" y="681" width="10" height="3" fill="#5fa3d8"/>
      <rect x="126" y="820" width="10" height="3" fill="#0a72ba"/>
    </g>

    <!-- input bars -->
    <g fill="#0a72ba">
      <rect x="196" y="821" width="56" height="137"/>
      <rect x="503" y="821" width="56" height="137"/>
      <rect x="809" y="821" width="56" height="137"/>
    </g>
    <g font-family="Montserrat, sans-serif" fill="#ffffff" font-size="17" font-style="italic">
      <text transform="translate(222 954) rotate(-90)"><tspan font-weight="800">$100</tspan> Worth</text>
      <text transform="translate(243 954) rotate(-90)" x="24">of Gas</text>
      <text transform="translate(529 954) rotate(-90)"><tspan font-weight="800">$100</tspan> Worth</text>
      <text transform="translate(550 954) rotate(-90)">of Electricity</text>
      <text transform="translate(835 954) rotate(-90)"><tspan font-weight="800">$100</tspan> Worth</text>
      <text transform="translate(856 954) rotate(-90)">of Electricity</text>
    </g>

    <!-- output bars -->
    <rect x="321" y="848" width="56" height="110" fill="url(#barRed)"/>
    <rect x="321" y="848" width="56" height="110" fill="url(#hatch)"/>
    <rect x="614" y="821" width="56" height="137" fill="url(#barRed)"/>
    <rect x="614" y="821" width="56" height="137" fill="url(#hatch)"/>
    <rect x="920" y="403" width="56" height="555" fill="url(#barRed)"/>
    <rect x="920" y="403" width="56" height="555" fill="url(#hatch)"/>

    <!-- callouts -->
    <g font-family="Montserrat, sans-serif" fill="#ffffff" font-style="italic" text-anchor="middle">
      <g transform="translate(245 742)">
        <use href="#callout-shape"/>
        <text x="76" y="24" font-size="18"><tspan font-weight="800" font-size="20">$80</tspan> Worth</text>
        <text x="72" y="46" font-size="17">of Heat</text>
      </g>
      <g transform="translate(536 716)">
        <use href="#callout-shape"/>
        <text x="76" y="24" font-size="18"><tspan font-weight="800" font-size="20">$100</tspan> Worth</text>
        <text x="72" y="46" font-size="17">of Heat</text>
      </g>
      <g transform="translate(843 302)">
        <use href="#callout-shape"/>
        <text x="76" y="24" font-size="18"><tspan font-weight="800" font-size="20">$400</tspan> Worth</text>
        <text x="72" y="46" font-size="17">of Heat</text>
      </g>
    </g>
  </svg>

  <div class="disclaimer">actual values may vary</div>

  <div class="system-label" style="left:137px;width:300px">80% Gas<br>Furnace</div>
  <div class="system-label" style="left:454px;width:289px">Electric<br>Heat</div>
  <div class="system-label" style="left:761px;width:302px">Our Best Selling<br>Heat Pump</div>

  <div class="cop-row" style="left:155px;width:278px"><div class="cop-pill">COP of .8</div></div>
  <div class="cop-row" style="left:461px;width:280px"><div class="cop-pill">COP of 1</div></div>
  <div class="cop-row" style="left:768px;width:278px"><div class="cop-pill">COP of 4</div></div>

  <div class="cop-note">COP Measure at <b>47°F</b></div>
</body>
</html>
```